Social Media Graphics - ALL TEXT RK

We are looking for a series of social media graphics for Instagram (standard size 1:1 (1080x1080px) that are ALL TEXT. We want the following quotes below on each graphic; one quote per graphic. AND, In very small letters at the bottom of each graphic, add @RKMarlowLive

The look and feel of these graphics should be complimentary to the color palette attached below; but keep them simple. But the design is up to you; at the end of this document, I provided various samples of all text graphics that I like as examples.

Target Market(s)

women looking to lose weight

Industry/Entity Type

health and wellness

Colors
E54698
E96AAD
F1A4CE
F9D9EA
FCEFF6

Requirements
Must have
• the quotes in the document
Should not have
• no stock photography

```html
<!DOCTYPE html>
<html lang="en">
<head>
<meta charset="utf-8">
<title>GLP-1 Social Graphics — RK</title>
<link rel="stylesheet" href="https://fonts.googleapis.com/css2?family=Montserrat:wght@500;600;700&family=Lato:wght@400&display=swap">
<style>
  :root {
    --stage: #3d3d3d;
    --blush: #fcedf4;
    --pink: #e54698;
    --pink-mid: #e96aad;
    --pink-soft: #f1a4ce;
    --pink-light: #f9d9ea;
    --ink: #1e1e1e;
    --white: #ffffff;
  }
  * { margin: 0; padding: 0; box-sizing: border-box; }
  html, body {
    width: 1200px; height: 1000px; overflow: hidden;
    background: var(--stage);
  }
  .post {
    position: absolute; top: 251px;
    width: 499px; height: 499px;
    background: var(--blush);
  }
  .post--intro { left: 91px; }
  .post--secret { left: 610px; }

  .organ-map { position: absolute; left: 0; top: 0; }
  .organ-icon {
    position: absolute; top: 118px;
    width: 94px; height: 80px;
    border-radius: 40px;
    background: radial-gradient(circle, var(--pink-light), var(--blush));
  }
  .organ-icon--brain { left: 50px; }
  .organ-icon--stomach { left: 205px; }
  .organ-icon--pancreas { left: 356px; }

  .message-card {
    position: absolute; left: 52px; top: 234px;
    width: 395px; height: 207px;
    background: var(--white);
    border-radius: 58px;
    box-shadow: 0 2px 3px rgba(229, 70, 152, 0.15);
    text-align: center;
    padding-top: 34px;
  }
  .message-card__text {
    font: 500 19px/25px "Montserrat", sans-serif;
    color: var(--ink);
    text-transform: uppercase;
    letter-spacing: 0.7px;
  }
  .message-card__cta {
    margin-top: 9px;
    font: 700 19px/25px "Montserrat", sans-serif;
    color: var(--pink);
    text-transform: uppercase;
    letter-spacing: 0.7px;
  }
  .handle {
    font: 400 14px/16px "Lato", sans-serif;
    color: var(--pink);
    letter-spacing: 0.4px;
  }
  .message-card .handle { margin-top: 18px; }

  .feature-art {
    position: absolute; left: 160px; top: 54px;
    width: 130px; height: 162px;
    background: linear-gradient(180deg, var(--pink-light) 0%, var(--pink-soft) 100%);
    opacity: 0.7;
  }
  .post__headline {
    position: absolute; left: 30px; right: 30px; top: 247px;
    text-align: center;
    font: 700 21px/27px "Montserrat", sans-serif;
    color: var(--pink);
    text-transform: uppercase;
    letter-spacing: 0.8px;
  }
  .post--secret .handle {
    position: absolute; left: 0; right: 0; top: 399px;
    text-align: center;
  }
</style>
</head>
<body>
  <section class="post post--intro">
    <svg class="organ-map" width="499" height="499" viewBox="0 0 499 499" aria-hidden="true">
      <path d="M98 101 V65 H406 V101 M252 65 V101" fill="none" stroke="var(--pink)" stroke-width="3"/>
    </svg>
    <div class="organ-icon organ-icon--brain" role="img" aria-label="Line icon of a brain"></div>
    <div class="organ-icon organ-icon--stomach" role="img" aria-label="Line icon of a stomach"></div>
    <div class="organ-icon organ-icon--pancreas" role="img" aria-label="Line icon of a pancreas"></div>

    <div class="message-card">
      <p class="message-card__text">A natural way to boost<br>GLP-1 - no injections, no side<br>effects, just real results.</p>
      <p class="message-card__cta">Here's how it works</p>
      <p class="handle">@RKMarlowLive</p>
    </div>
  </section>

  <section class="post post--secret">
    <div class="feature-art" role="img" aria-label="Illustration of a capsule holding bathroom scales"></div>
    <h2 class="post__headline">GLP-1: The magic behind the<br>weight loss drugs. But<br>here's the secret - you can<br>boost it naturally with-<br>out a prescription!</h2>
    <p class="handle">@RKMarlowLive</p>
  </section>
</body>
</html>
```